HARLOWE CONSERVATORY SAXOPHONE SENIOR RECITAL

I need a poster design for my senior saxophone recital. The title of it is "Quill: a Voyage beneath the Edge of Tone". My concept is completely contrasting to the idea of a typical university recital. I'm so put off by the idea of "clap..clap..{play some music}..clap..clap..repeat". My recital is all based off of sound. The music I selected is all very modern (i.e Brem Ostrakel 'Warm from the First Pour' for Saxophone and Coffee Machine). I've included the Chatterbox link so you can see the picture I have in the background. I like the idea of minimal black and white photography. Also, I would like the time / date / location / etc. all included on it. Let your imaginations run wild! It's art for an artist!
https://www.chatterbox-example.net/events/412093857716230/
Target Market(s)
University Students around the Harlowe Conservatory and locals around the art district of South Beach, FL.
Industry/Entity Type
University
Look and feel

```html
<!DOCTYPE html>
<html lang="en">
<head>
<meta charset="utf-8">
<title>Quill: a Voyage beneath the Edge of Tone — Senior Saxophone Recital</title>
<link rel="stylesheet" href="https://fonts.googleapis.com/css2?family=Bebas+Neue&family=Share+Tech+Mono&family=Cutive+Mono&display=swap">
<style>
  :root {
    --page: #ffffff;
    --ink: #111111;
    --sky-light: #cfcfcf;
    --sky-dark: #1a1a1a;
    --forest: #2b2b2b;
    --water: #0d0d0d;
    --veil: rgba(150, 150, 150, 0.62);
  }
  * { margin: 0; padding: 0; box-sizing: border-box; }
  html, body { width: 1200px; height: 1000px; overflow: hidden; background: var(--page); }
  .poster { position: relative; width: 1200px; height: 1000px; background: var(--page); }

  .backdrop {
    position: absolute; left: 215px; top: 0; width: 772px; height: 1000px;
    background:
      radial-gradient(ellipse 40% 12% at 50% 60%, rgba(220,220,220,0.55), transparent 70%),
      linear-gradient(90deg, rgba(0,0,0,0.75) 0%, rgba(0,0,0,0) 22%, rgba(0,0,0,0) 78%, rgba(0,0,0,0.75) 100%),
      linear-gradient(180deg, var(--sky-dark) 0%, #555 8%, var(--sky-light) 18%, #9a9a9a 32%, #b5b5b5 48%, var(--forest) 58%, #3a3a3a 62%, var(--water) 78%, #222 92%, #4a4a4a 100%);
  }

  .veil {
    position: absolute; left: 329px; top: 182px; width: 547px; height: 633px;
    background: var(--veil);
  }

  .line {
    position: absolute; left: 329px; width: 547px; text-align: center;
    color: var(--ink); white-space: nowrap;
  }
  .mono { font-family: "Share Tech Mono", "Cutive Mono", monospace; font-size: 26px; line-height: 1; letter-spacing: 0.5px; }
  .list { font-family: "Share Tech Mono", "Cutive Mono", monospace; font-size: 23px; line-height: 1; }
  .list-head { font-style: italic; }
  .display { font-family: "Bebas Neue", "Oswald", sans-serif; line-height: 1; }
  .title-main { font-size: 134px; letter-spacing: 2px; }
  .title-sub { font-size: 46px; letter-spacing: -0.5px; }
  .divider { font-size: 20px; line-height: 1; }
</style>
</head>
<body>
<main class="poster">
  <div class="backdrop" role="img" aria-label="Black and white photograph of a still forest lake with tall trees reflected in dark water"></div>
  <div class="veil"></div>

  <header>
    <p class="line mono" style="top:196px;">MARCO DELLAVISTA SENIOR</p>
    <p class="line mono" style="top:221px;">SAXOPHONE RECITAL</p>
    <h1>
      <span class="line display title-main" style="top:256px;">QUILL:</span>
      <span class="line display title-sub" style="top:372px;">A VOYAGE BENEATH THE</span>
      <span class="line display title-sub" style="top:412px;">EDGE OF TONE</span>
    </h1>
  </header>

  <p class="line divider" style="top:472px;" aria-hidden="true">❖</p>

  <section class="event-details">
    <p class="line mono" style="top:506px;">SUNDAY DECEMBER 8, 2013</p>
    <p class="line mono" style="top:533px;">EDWIN R. HALE RECITAL HALL</p>
  </section>

  <p class="line divider" style="top:571px;" aria-hidden="true">❖</p>

  <section class="program">
    <p class="line list list-head" style="top:606px;">WORKS BY:</p>
    <p class="line list" style="top:631px;">Oreste Vallarno</p>
    <p class="line list" style="top:656px;">Dr. Glenn Parrow *WORLD PREMIERE*</p>
    <p class="line list" style="top:681px;">Brem Ostrakel</p>
    <p class="line list" style="top:706px;">Dr. Lorna Whitcombe*WORLD PREMIERE*</p>
    <p class="line list" style="top:731px;">Silas Ferrand</p>
    <p class="line list" style="top:756px;">--INTERMISSION--</p>
    <p class="line list" style="top:781px;">Harold Breck</p>
  </section>
</main>
</body>
</html>
```